Table top flyer including information on bourbon and cocktail menu

K&T SMOKEHOUSE is the original Asadería and the only restaurant chain in Mexico focused on providing a uniquely Southern (US) dining experience. We need a table top flyer in Spanish that will help engage and educate our customers (Mexicans) about American whiskey´s including Bourbon, Tennessee Whiskey, American Rye and Moonshine as well as serve as a drink and cocktail menu. The overall objective of the flyer is to educate, create interest and spur trial. The attached documents provide good direction in terms of design and content that should be included. See our facebook page for more photos and inspiration. www.vexlo.example/KTSMOKEGDL

Target Market(s)

K&T SMOKEHOUSE is the original Asadería and the only restaurant chain in Mexico focused on providing a uniquely Southern (US) dining experience. Our specialty is baby back ribs served with a number of traditional southern sides including baked beans, corn bread, organic green salad, home cut fries and corn on the cob. We are also introducing Mexico to the culture of American whiskey and folk music with our Bourbon Bar where we offer a wide selection Straight Kentucky Bourbon, Tennessee Whiskey and American Rye Whiskey. Our customers are primarily from 25 to 45 year old Mexicans ranging from middle to upper income and educated.

Industry/Entity Type

Restaurant

Requirements
Must have
• The design should communicate the uniqueness of the Southern (US) culture and how American Whiskey and related cocktails play a part of that culture. Furthermore it should position K&T SMOKEHOUSE as an expert on the topic. The price for all the whiskeys is $60 pesos and we offer Straight Kentucky Bourbon, Tennessee Whiskey, American Rye Whiskey and Moonshine. Our cocktails cost $70 pesos and include the Old Fashioned, Mint Julep and the Derby. The flyer should have 4 faces and be able to stand on its own on the table. We want each cocktail to have a descriptive illustration similar to the images attached.

```html
<!DOCTYPE html>
<html lang="es">
<head>
<meta charset="utf-8">
<title>K&amp;T Smokehouse — Conoce tu whiskey</title>
<link rel="stylesheet" href="https://fonts.googleapis.com/css2?family=Stint+Ultra+Condensed&family=Oswald:wght@600&family=Pathway+Gothic+One&display=swap">
<style>
:root{
  --page:#ffffff;
  --sheet:#4a4a4a;
  --panel:#161616;
  --panel-light:#262626;
  --cream:#f7e6a2;
  --ink:#f2f2f2;
  --rule:#9a9a9a;
  --ornament:#4a4a4a;
}
*{box-sizing:border-box;margin:0;padding:0}
html,body{width:1200px;height:900px;overflow:hidden;background:var(--page)}
.flyer{position:relative;width:1200px;height:900px}
.sheet{position:absolute;left:22px;top:40px;width:1156px;height:820px;background:var(--sheet)}
.band{position:absolute;left:22px;width:1156px;height:18px;
  background:repeating-linear-gradient(90deg,#111 0 3px,#4a4a4a 3px 5px);border:1px solid #000}
.band--top{top:40px}.band--bottom{top:842px}
.face{position:absolute;top:58px;height:784px;overflow:hidden;
  background:radial-gradient(ellipse at 50% 40%,var(--panel-light),var(--panel) 75%);
  color:var(--ink);font-family:"Pathway Gothic One",sans-serif;text-align:center}
.face--cover{left:22px;width:288px}
.face--bourbon{left:312px;width:286px}
.face--rye{left:600px;width:287px}
.face--cocktails{left:889px;width:289px}
.hero{position:absolute;left:0;width:100%;font-family:"Stint Ultra Condensed",serif;font-weight:400;color:var(--cream);
  text-shadow:2px 2px 0 #000,4px 4px 0 #555;line-height:.86;transform:rotate(-10deg)}
.hero--cover{top:200px;font-size:96px}
.hero--cocktails{top:40px;font-size:76px}
.ornament{position:absolute;left:50%;transform:translateX(-50%);height:10px;
  background:linear-gradient(90deg,transparent,var(--ornament) 30%,var(--ornament) 70%,transparent);opacity:.7;border-radius:5px}
.price{position:absolute;width:70px;height:70px}
.price svg{position:absolute;inset:0}
.price__value{position:absolute;top:10px;width:100%;font-family:"Oswald",sans-serif;font-size:32px;color:var(--cream);line-height:1}
.price__unit{position:absolute;top:46px;width:100%;font-size:11px;letter-spacing:1px}
.brand{position:absolute;left:60px;top:620px;width:170px;color:#8c8c8c}
.brand__dot{display:block;margin:0 auto 6px;width:16px;height:16px;border:2px solid #8c8c8c;border-radius:50%}
.brand__name,.brand__kind{font-size:17px;letter-spacing:1px;line-height:20px}
.section{position:absolute;left:0;width:100%}
.section__title{font-family:"Oswald",sans-serif;font-weight:600;font-size:32px;line-height:36px;color:var(--cream);text-shadow:2px 2px 0 #000;letter-spacing:1px}
.section__body{width:236px;margin:26px auto 0;font-size:10.3px;line-height:12.6px;letter-spacing:.2px}
.section__body p+p{margin-top:12.6px}
.stars{position:absolute;left:0;width:100%;font-size:11px;letter-spacing:4px;color:#777}
.menu{position:absolute;left:47px;top:275px;width:190px;height:500px;border-left:1px solid var(--rule);border-right:1px solid var(--rule);border-bottom:1px solid var(--rule)}
.drink{position:absolute;left:0;width:100%}
.drink__name{height:39px;border-top:1px solid var(--rule);border-bottom:1px solid var(--rule);white-space:nowrap;
  font-family:"Oswald",sans-serif;font-weight:600;font-size:20px;line-height:37px;letter-spacing:1px;color:var(--cream)}
.drink__art{position:absolute;left:12px;top:56px;width:66px;height:78px;border-radius:8px;
  background:linear-gradient(#3a3a3a,#262626)}
.drink__recipe{position:absolute;left:97px;top:74px;text-align:left;list-style:none;font-size:12.5px;line-height:14px;letter-spacing:.5px;white-space:nowrap}
</style>
</head>
<body>
<main class="flyer">
  <div class="sheet"></div>
  <div class="band band--top"></div>

  <section class="face face--cover">
    <div class="ornament" style="top:168px;width:240px" role="img" aria-label="Adorno caligráfico"></div>
    <h1 class="hero hero--cover">KNOW<br>YOUR<br>WHISKEY</h1>
    <div class="ornament" style="top:528px;width:250px" role="img" aria-label="Adorno caligráfico"></div>
    <div class="price" style="left:181px;top:478px">
      <svg viewBox="0 0 70 70"><circle cx="35" cy="35" r="33" fill="#161616" stroke="#fff" stroke-width="2" stroke-dasharray="3 2"/><circle cx="35" cy="35" r="28" fill="none" stroke="#fff" stroke-width="1"/></svg>
      <div class="price__value">60</div><div class="price__unit">PESOS</div>
    </div>
    <div class="brand">
      <span class="brand__dot"></span>
      <div class="brand__name">K&amp;T SMOKEHOUSE</div>
      <div class="brand__kind">ASADERÍA</div>
    </div>
  </section>

  <section class="face face--bourbon">
    <div class="section" style="top:24px">
      <h2 class="section__title">STRAIGHT<br>KENTUCKY<br>BOURBON</h2>
      <div class="ornament" style="top:114px;width:230px" role="img" aria-label="Adorno caligráfico"></div>
      <div class="section__body">
        <p>El bourbon es una bebida destilada de la familia de los whiskeys, se caracteriza por ser ligeramente aromático y de sabor acaramelado. El bourbon whiskey, según la ley estadounidense, debe ser elaborado a base de maíz por lo menos en una concentración entre el 50% y, generalmente, al 70%.</p>
        <p>Otros ingredientes añadidos son, típicamente: el trigo, centeno o cebada malteada. Su periodo de envejecimiento suele ser como mínimo dos años, no existen requerimientos legales para este periodo mínimo y que el producto final se denomine "bourbon" pero sí existen requerimientos para denominarlo straight bourbon. Por regla general el bourbon se madura durante un periodo de 5 años en barricas de roble que pueden ser nuevas y/o tostadas.</p>
        <p>El nombre de la bebida destilada proviene del lugar de Estados Unidos donde se produce de forma originaria Bourbon County (Kentucky) (que, a su vez, toma su nombre de la familia real de la Casa de Borbón).</p>
      </div>
    </div>
    <div class="stars" style="top:404px">★★★★★★★★★★★★★★★★★★</div>
    <div class="section" style="top:430px">
      <h2 class="section__title">TENNESSEE<br>WHISKEY</h2>
      <div class="ornament" style="top:66px;width:230px" role="img" aria-label="Adorno caligráfico"></div>
      <div class="section__body">
        <p>El Tennessee Whiskey es un straight bourbon, lo que obliga a envejecer el destilado un mínimo de 2 años dentro de la barrica. Por lo demás, las normas de producción son las mismas que las del bourbon de Kentucky con dos salvedades.</p>
        <p>La primera, que para denominarse Tennessee Whiskey si es obligatorio que se haya producido, destilado y embotellado en el estado de Tennessee. La segunda, que antes de introducir el whiskey en la barrica para su añejamiento, éste es filtrado a través de una columna de 3 metros de carbón vegetal de madera de arce. De esta forma adquiere un aroma más suave y sabor más dulce que el bourbon de Kentucky.</p>
        <p>Los barriles de whisky se fabrican con roble blanco de América debido a que esta madera tiene la combinación necesaria de compuestos para lograr el producto final. Mientras el whisky se añeja dentro del barril, la madera se contrae y expande según los cambios climáticos que se produzcan en su entorno.</p>
      </div>
    </div>
  </section>

  <section class="face face--rye">
    <div class="section" style="top:24px">
      <h2 class="section__title">AMERICAN<br>RYE WHISKEY</h2>
      <div class="ornament" style="top:78px;width:230px" role="img" aria-label="Adorno caligráfico"></div>
      <div class="section__body">
        <p>El método de destilación es similar al de bourbon en prácticamente todo, y la gente suele confundirlos. La diferencia más notable es que el American Rye whiskey debe ser elaborado a base de cebada por lo menos en una concentración del 51%.</p>
        <p>En los 1700´s y 1800s el rye whiskey era el whiskey preferido en los estados del noreste de los Estados Unidos incluyendo Pensilvania y Maryland. Jeremiah Holloway, el primer productor de los EEUU hacía rye whiskey en su hacienda Holloway Hill.</p>
        <p>Originalmente todos los principales cocteles americanos como son el Old Fashioned, Manhattan y Whiskey Sours se hacían de rye pero con la introducción del bourbon en los estados del norte los barman empezaron a sustituir el bourbon por el rye.</p>
        <p>Rey está reconocido por añadir lo que muchos llaman un sabor picante o frutoso al whiskey. El bourbon hecho a base de mínimo 51% maíz tiene un sabor más dulce y con mas cuerpo que el Rye que es mas seco. Debido a su sabor distinto a veces se refiere al American Rye Whiskey como el equivalente americano de un Islay whisky del sur de Escocia.</p>
      </div>
    </div>
    <div class="stars" style="top:418px">★★★★★★★★★★★★★★★★★★</div>
    <div class="section" style="top:440px">
      <h2 class="section__title">APPALACHIAN<br>MOONSHINE</h2>
      <div class="ornament" style="top:66px;width:230px" role="img" aria-label="Adorno caligráfico"></div>
      <div class="section__body">
        <p>Moonshine, white lightning, white mule, hooch, y Tennessee white whiskey son términos para describir alcoholes de alto grado que están destilado de manera ilegal. La palabra "moonshine" proviene de la palabra "moonrakers" que fue usado para describir los contrabandistas (que trabajaban bajo la luz de la luna) y las operaciones clandestinas usadas por las destilerías ilegales en la zona de Apalachina en el sureste de Estados Unidos.</p>
        <p>Moonshine es muy potente debido al hecho de que no se corta ni se madura. Cuando sale de la destilería por la ultima vez es totalmente transparente y tiene entre 150 y 170 grados. Muchos dicen que en los viejos tiempos los contrabandistas lo utilizaban como gasolina y es por eso que las policías nunca los pudieron agarrar. Por otro lado el deporte de las carreras de stock car creció en el sur de los EEUU por algo.</p>
      </div>
    </div>
  </section>

  <section class="face face--cocktails">
    <h1 class="hero hero--cocktails">BOURBON<br>COCKTAILS</h1>
    <div class="price" style="left:176px;top:192px">
      <svg viewBox="0 0 70 70"><circle cx="35" cy="35" r="33" fill="#161616" stroke="#fff" stroke-width="2" stroke-dasharray="3 2"/><circle cx="35" cy="35" r="28" fill="none" stroke="#fff" stroke-width="1"/></svg>
      <div class="price__value">70</div><div class="price__unit">PESOS</div>
    </div>
    <div class="menu">
      <div class="drink" style="top:0">
        <h3 class="drink__name">THE OLDFASHIONED</h3>
        <div class="drink__art" role="img" aria-label="Ilustración de un vaso old fashioned con hielo y rodaja de naranja"></div>
        <ul class="drink__recipe"><li>SUGAR CUBE</li><li>BITTERS</li><li>WATER</li><li>BOURBON</li></ul>
      </div>
      <div class="drink" style="top:160px">
        <h3 class="drink__name">MINT JULEP</h3>
        <div class="drink__art" role="img" aria-label="Ilustración de un vaso de mint julep con hielo picado y menta"></div>
        <ul class="drink__recipe" style="top:76px"><li>MINT LEAVES</li><li>BROWN SUGAR</li><li>BOURBON</li></ul>
      </div>
      <div class="drink" style="top:320px">
        <h3 class="drink__name">THE DERBY</h3>
        <div class="drink__art" role="img" aria-label="Ilustración de una copa de cóctel con rodaja de toronja"></div>
        <ul class="drink__recipe" style="top:76px"><li>BOURBON</li><li>GRAPEFRUIT JUICE</li><li>HONEY</li></ul>
      </div>
    </div>
  </section>

  <div class="band band--bottom"></div>
</main>
</body>
</html>
```